Dental Smile Compass Brochure

We need an updated brochure/flyer for our in house dental health membership. We also want to start marketing this to businesses and will need one specifically targeted to businesses as well. Our company colors we need to start branding are red, black and white, however, we don't want the brochure to be too busy with color. We are open to ideas and want something different and eye catching.

Industry/Entity Type

Dental

Font styles to use
Serif

Colors
ec1f27
ffffff
000000

Requirements
Must have
• Brand colors; red, black and white, must have our company logo,
Should not have
• vague and random stock photos

```html
<!DOCTYPE html>
<html lang="en">
<head>
<meta charset="utf-8">
<title>Dental Smile Compass – Membership Plan Brochure</title>
<link href="https://fonts.googleapis.com/css2?family=Arimo:ital,wght@0,400;0,700;1,400&display=swap" rel="stylesheet">
<style>
  :root{
    --brand-red:#ec1f27;
    --brand-red-deep:#c4161c;
    --ink:#1a1a1a;
    --black:#000000;
    --white:#ffffff;
    --grey-light:#cfcfd0;
    --grey-dark:#9a9a9c;
  }
  *{box-sizing:border-box;margin:0;padding:0}
  html,body{width:1200px;height:849px;overflow:hidden;background:var(--white)}
  .brochure{position:relative;width:1200px;height:849px;overflow:hidden;
    font-family:"Arimo",Arial,sans-serif;color:var(--ink);font-size:14px;line-height:21px}
  .backdrop{position:absolute;inset:0;width:1200px;height:849px}
  .panel{position:absolute;top:28px;width:343px;height:792px;background:var(--white);
    padding:31px 26px 0 26px}
  .panel--left{left:28px}
  .panel--middle{left:428px}
  .panel--right{left:828px;padding-top:27px}
  .section-title{background:var(--brand-red);color:var(--white);font-weight:700;
    font-size:19px;line-height:28px;height:28px;padding-left:8px;letter-spacing:.1px;
    margin-bottom:5px}
  .section + .section{margin-top:21px}
  .bullets{list-style:none}
  .bullets li{position:relative;padding-left:12px}
  .bullets li::before{content:"•";position:absolute;left:0;top:0}
  .bullets--spaced li{margin-bottom:4px}
  .bullets--tight li{margin-bottom:0}
  .lead{font-weight:700;margin:0 0 4px}
  .gap-top{margin-top:13px}
  .copy{margin-bottom:4px}
  .price-label{font-weight:700;margin-top:4px}
  .footnote{font-style:italic;margin-top:12px}
  strong{font-weight:700}
</style>
</head>
<body>
<main class="brochure">
  <svg class="backdrop" viewBox="0 0 1200 849" aria-hidden="true">
    <defs>
      <linearGradient id="greyFade" x1="0" y1="0" x2="1" y2="0">
        <stop offset="0" stop-color="#a3a3a5"/>
        <stop offset=".5" stop-color="#d4d4d5"/>
        <stop offset="1" stop-color="#a3a3a5"/>
      </linearGradient>
      <linearGradient id="redFade" x1="0" y1="0" x2="0" y2="1">
        <stop offset="0" stop-color="#ec1f27"/>
        <stop offset="1" stop-color="#c4161c"/>
      </linearGradient>
    </defs>
    <rect width="1200" height="849" fill="url(#greyFade)"/>
    <path d="M0 440 C200 520 360 610 600 636 C800 650 1000 600 1200 530 L1200 849 L0 849Z" fill="var(--black)"/>
    <path d="M0 456 C200 536 360 622 600 644 C800 656 1000 612 1200 545 L1200 849 L0 849Z" fill="var(--white)"/>
    <path d="M0 470 C200 552 360 636 600 656 C800 668 1000 626 1200 560 L1200 849 L0 849Z" fill="url(#redFade)"/>
  </svg>

  <section class="panel panel--left">
    <div class="section">
      <h2 class="section-title">ADVANTAGES:</h2>
      <ul class="bullets bullets--spaced">
        <li><strong>It’s not insurance;</strong> no third party;<br>no red tape</li>
        <li><strong>Affordable</strong> predictable cost,<br>automatic payments</li>
        <li><strong>No waiting period</strong></li>
        <li><strong>No deductible ever</strong></li>
        <li><strong>No annual maximum</strong></li>
        <li><strong>No-claim forms,</strong> no claims to be denied,<br>no stalled payments</li>
        <li><strong>No</strong> pre-authorizations</li>
        <li>Choice of coverage to fit your needs;<br>tailor your plan to fit you</li>
        <li>Know your exact coverage before treatment</li>
        <li><strong>You choose</strong> the treatment; no third party<br>interference</li>
        <li>Includes benefits for cosmetic dentistry and orthodontics, and other services usually not included in dental insurance plans</li>
      </ul>
    </div>
    <div class="section">
      <h2 class="section-title">WHAT’S INCLUDED?</h2>
      <p class="lead">Preventive services at 100%:</p>
      <ul class="bullets bullets--tight">
        <li>Your regular twice-a-year cleanings or<br>4-times-a-year periodontal maintenance</li>
        <li>Dental exam by the doctor each year</li>
        <li>Necessary x-rays</li>
        <li>Fluoride treatments</li>
      </ul>
      <p class="lead gap-top">Plus:</p>
      <ul class="bullets bullets--tight">
        <li>Teeth whitening - 50% off</li>
        <li>Benefits for <strong>fillings, crowns, bridges, orthodontics, veneers and implants</strong></li>
      </ul>
    </div>
  </section>

  <section class="panel panel--middle">
    <div class="section">
      <h2 class="section-title">HOW DO I QUALIFY?</h2>
      <ul class="bullets bullets--spaced">
        <li>You must be a patient of record of Linwood Dental Care in good standing (you may sign up after your initial exam, if you are a new patient)</li>
      </ul>
      <p class="lead">You agree to partner with us to create the savings:</p>
      <ul class="bullets bullets--spaced">
        <li>Keep your appointments with us on time as scheduled</li>
        <li>Keep your account balance zero by paying at the time of service or before</li>
        <li>No insurance claims to file.</li>
      </ul>
      <p class="copy">If you do have insurance, you may still qualify if you file claims yourself (we will print the form for you), and make payment to us in full before treatment. The insurance payment will then go to you.</p>
    </div>
    <div class="section">
      <h2 class="section-title">HOW DOES IT WORK?</h2>
      <ul class="bullets bullets--spaced">
        <li>Yearly membership fee divided into<br>12 monthly payments</li>
        <li>Monthly payments charged to your credit or debit card automatically, or automatic withdrawals from your bank account</li>
        <li>Membership renews each year automatically</li>
        <li><strong>Basic Plan</strong> includes: 100% coverage for two cleanings and fluoride treatments per year, x-rays, and one exam by the doctor</li>
        <li><strong>Periodontal Maintenance Plan</strong> includes: 100% coverage for four periodontal maintenance visits per year, x-rays, fluoride treatments, doctor exam</li>
      </ul>
    </div>
  </section>

  <section class="panel panel--right">
    <div class="section">
      <ul class="bullets bullets--spaced">
        <li>Nothing to pay when you come for your regular visit with the hygienist</li>
        <li><strong>Both plans</strong> include benefits for all other services we offer</li>
        <li>Includes benefits for elective treatment not covered by most dental insurance plans</li>
        <li><strong>No yearly maximum</strong> on benefits</li>
        <li>Benefits are clearly spelled out; no guessing</li>
        <li>Membership benefits apply only to services provided directly by Linwood Dental Care in our office</li>
      </ul>
    </div>
    <div class="section">
      <h2 class="section-title">WHAT’S THE CATCH?</h2>
      <p class="copy">No catch, no hidden costs.<br>This plan reflects the fact that those who meet the conditions outlined above reduce our costs. These savings are passed back to you .</p>
    </div>
    <div class="section">
      <h2 class="section-title">WHAT’S THE COST?</h2>
      <p><strong>Set-up Fee</strong> (applies to all plans)</p>
      <ul class="bullets bullets--tight"><li>$45 per person, $90 maximum per family</li></ul>
      <p class="price-label">Basic preventive plan:</p>
      <p>two preventive visits per year, restorative benefits:</p>
      <ul class="bullets bullets--tight"><li>Individual: $27 per month</li></ul>
      <p class="price-label">Periodontal maintenance plan:</p>
      <p>four maintenance visits/yr., restorative benefits:</p>
      <ul class="bullets bullets--tight"><li>Individual: $52 per month</li></ul>
      <p class="price-label">Children* (under 18), basic preventive plan:</p>
      <ul class="bullets bullets--tight"><li>$20 per month</li></ul>
      <p class="footnote">*Immediate family living in same household as parent who is a member of this plan</p>
    </div>
  </section>
</main>
</body>
</html>
```